Larkwell cyber security firm Website

We did our website ourselves on Joomla, it's not great. We want a wordpress based redesign. Some thing that will represent a modern cyber security firm that's aimed at solving business problems.
Https://larkwell.co.nz (current site)
#58427c - primary color (you'll know why when you see it's name)
Logo files can be provided. Ask for more info if you need.

We want a modern, quick to load website. Website is going to have a home - services - products - about us - blogs menu. Will need a footer menu, site map, contact page etc.
We getting Content done sperately.
Our logo is #58427c - so hoping for a light theme (or at least the top is).
While we have been specific around the color - we are not after a website that has too much of it.

Reference sites that we like :
https://www.tidemoor.co.nz/ - Love the full screen real world image
https://venlorix.co.nz/ (love the real world imagry and motion)
https://www.qavrel.com/us-en?lnk=m
https://ostwynde.com

Please dont use :
cartoon or redered images : (Like this : https://img.plumdexa.com/free-vector/cyber-security-concept_23-2148543851.jpg?w=2000 )

Please don't use images like this : https://www.merivast.com/eu/blog/oil-gas/app/uploads/2020/04/116137226_s-1440x564_c.jpg - they are old and boring.

We would like to see some creativity - loading our logo into a readymade wordpress template and hitting go won't cut it.

Thanks everyone who has submitted so far. We've extended the deadline as we wanted to give everyone a chance to Re- read the brief and perhaps make some tweeks should they feel it necessary.

Target Market(s)

Mid - large enterprise, finance, insurance, utilities vertical

Industry/Entity Type

Cyber security

Coding

Coded - Design and coding required

Number of Pages Required

5+ page

Font styles to use
Other font styles liked:
• Open sans

Colors

Designer to choose colors to be used in the design.

Requirements
Must have
• Simple clear messaging, something that catches user engagement
Nice to have
• Motion of some sort, but not overdone, GDPR

```html
<!DOCTYPE html>
<html lang="en">
<head>
<meta charset="utf-8">
<title>Larkwell – Cyber Security</title>
<link rel="stylesheet" href="https://fonts.googleapis.com/css2?family=Epilogue:wght@300;400;500;600&display=swap">
<style>
:root{
  --primary:#58427c;
  --primary-soft:#7a63a3;
  --ink:#2b2b2b;
  --muted:#555;
  --line:#b9b0c9;
  --white:#fff;
}
*{box-sizing:border-box;margin:0;padding:0}
html,body{width:1200px;height:3889px;overflow:hidden}
body{font-family:"Epilogue",sans-serif;color:var(--ink);background:var(--white);position:relative}
.abs{position:absolute}
a{color:inherit;text-decoration:none}

/* header + hero */
.hero{left:0;top:0;width:1200px;height:713px;background:linear-gradient(100deg,#173a6a 0%,#1f4f86 30%,#2a3f62 55%,#1c2236 80%,#2b2433 100%)}
.hero-glow{left:560px;top:140px;width:640px;height:573px;background:radial-gradient(ellipse at 70% 70%,rgba(240,170,80,.35),rgba(0,0,0,0) 60%)}
.brand{left:98px;top:26px;display:flex;align-items:center;gap:10px;color:var(--white);font-size:32px;font-weight:500;letter-spacing:1px}
.brand-dot{width:34px;height:34px;border:3px solid currentColor;border-radius:50%}
.nav{top:34px;left:0;width:1200px;font-size:15px;color:var(--white)}
.nav a{position:absolute}
.hero-title{left:98px;top:218px;width:520px;color:var(--white);font-size:51px;font-weight:400;line-height:59px}
.hero-sub{left:98px;top:416px;width:350px;color:var(--white);font-size:16px;line-height:25px;font-weight:300}
.btn{display:flex;align-items:center;justify-content:center;gap:10px;background:var(--primary-soft);color:var(--white);border-radius:24px;font-size:13px;text-transform:uppercase;font-weight:400}
.btn svg{width:16px;height:16px}
.hero-btn{left:98px;top:516px;width:149px;height:46px}

/* about */
.about-photo{left:98px;top:805px;width:477px;height:471px;border:3px solid var(--primary);background:linear-gradient(135deg,#0d2f66,#1b4f94 45%,#233a63 70%,#0e1c38)}
.eyebrow-line{display:flex;align-items:center;gap:14px;color:var(--primary);font-size:17px}
.eyebrow-line i{display:block;height:1px;background:var(--primary-soft)}
.about-eyebrow{left:625px;top:806px;width:477px;color:var(--ink)}
.about-title{left:625px;top:838px;width:490px;font-size:35px;line-height:43px;color:var(--primary);font-weight:400;letter-spacing:-.3px}
.about-text{left:625px;width:477px;font-size:11.3px;line-height:18.7px;color:var(--ink);text-align:justify;font-weight:300}
.about-btn{left:625px;top:1230px;width:149px;height:46px}

/* section heads */
.section-head{left:0;width:1200px;text-align:center}
.section-head .eyebrow-line{justify-content:center;font-size:17px}
.section-head .eyebrow-line i{width:72px}
.section-head h2{font-size:42px;font-weight:400;color:var(--primary);margin-top:8px;letter-spacing:.5px}

/* services */
.svc-arrow{top:1632px;width:36px;height:36px;border:2px solid var(--primary);border-radius:50%;display:flex;align-items:center;justify-content:center}
.svc-card-hl{left:440px;top:1561px;width:319px;height:201px;background:linear-gradient(180deg,#6b5294,#4a3470);border-radius:3px}
.svc-icon{top:1505px;width:106px;height:106px;border-radius:50%;background:var(--white);border:3px solid var(--primary);display:flex;align-items:center;justify-content:center}
.svc-icon.dark{background:var(--primary);border-color:var(--white);box-shadow:0 0 0 3px var(--primary)}
.svc-title{top:1629px;width:280px;text-align:center;font-size:16px;color:var(--primary)}
.svc-text{top:1662px;width:270px;text-align:center;font-size:11px;line-height:17px;color:var(--ink);font-weight:300}
.on-dark{color:var(--white)}
.svc-next{left:588px;top:1750px;width:24px;height:24px;border-radius:50%;background:var(--white);display:flex;align-items:center;justify-content:center}

/* products */
.prod-icon{top:2015px;width:116px;height:116px}
.prod-num{top:2162px;width:40px;height:40px;border-radius:50%;background:var(--primary);color:var(--white);display:flex;align-items:center;justify-content:center;font-size:16px}
.prod-name{top:2225px;width:220px;text-align:center;font-size:18.5px;line-height:24px;color:var(--ink)}
.prod-link{top:2075px;width:84px;height:30px}

/* articles */
.art-photo{border-radius:4px;overflow:hidden}
.art-photo.big{left:100px;top:2482px;width:488px;height:293px;background:linear-gradient(120deg,#0f2b5c,#1e4fa0 40%,#163a74 70%,#0a1a3a)}
.art-photo.sm1{left:612px;top:2482px;width:232px;height:216px;background:linear-gradient(135deg,#d8dbe2,#9aa1ad 60%,#6e7685)}
.art-photo.sm2{left:612px;top:2731px;width:232px;height:216px;background:linear-gradient(135deg,#8ea8e6,#4f66c7 50%,#2c3d93)}
.date-tag{position:absolute;left:10px;bottom:14px;background:rgba(88,66,124,.92);color:var(--white);font-size:13px;padding:5px 10px}
.art-cat{font-size:9.5px;letter-spacing:2px;color:#666;text-transform:uppercase}
.art-title{font-size:23px;line-height:29px;color:var(--ink);font-weight:400}
.art-text{font-size:10.5px;line-height:16.5px;color:#555;font-weight:300}
.art-btn{width:112px;height:32px;font-size:10px;gap:8px}
.art-btn svg{width:12px;height:12px}

/* contact */
.contact{left:0;top:3028px;width:1200px;height:519px;background:linear-gradient(180deg,#5d4788 0%,#55407f 50%,#4c3873 100%)}
.contact-shade{left:0;top:3250px;width:1200px;height:297px;background:linear-gradient(180deg,rgba(60,44,92,0),rgba(60,44,92,.55))}
.field{background:var(--white);border:1px solid #d6d0e2;font-size:11px;color:#888;padding:12px 11px;letter-spacing:.5px}
.send{left:322px;top:3442px;width:557px;height:40px;background:var(--primary-soft);color:var(--white);font-size:12px;display:flex;align-items:center;justify-content:center;font-weight:600;letter-spacing:.5px}

/* footer */
.foot-h{font-size:16px;font-weight:600;color:var(--primary);letter-spacing:.3px}
.foot-links{font-size:14px;line-height:25.5px;color:var(--ink)}
.foot-div{top:3600px;width:1px;height:190px;background:#d6d0e2}
.contact-row{display:flex;gap:12px;font-size:13.5px;line-height:19px;color:var(--ink)}
.contact-row svg{flex:0 0 16px;height:16px;margin-top:2px}
.map{left:563px;top:3595px;width:224px;height:180px;border:3px solid var(--primary);border-radius:6px;background:linear-gradient(135deg,#eef0f2,#e3e6e9)}
.foot-mark{left:946px;top:3592px;width:48px;height:48px;border:4px solid var(--primary);border-radius:50%}
.foot-brand{left:830px;top:3654px;width:280px;text-align:center;font-size:38px;line-height:44px;font-weight:500;color:var(--primary);letter-spacing:1.5px}
.follow{left:882px;top:3733px;display:flex;align-items:center;gap:8px;font-size:16px;color:var(--primary)}
.follow span.s{width:22px;height:22px;border-radius:50%;background:var(--primary)}
.bottom-bar{left:0;top:3825px;width:1200px;height:64px;background:var(--primary);color:var(--white);font-size:12.5px;display:flex;align-items:center;justify-content:center}
</style>
</head>
<body>

<!-- HEADER / HERO -->
<section class="hero abs" role="img" aria-label="Night aerial photograph of a coastal city skyline with beach and lit towers"></section>
<div class="hero-glow abs"></div>
<div class="brand abs"><span class="brand-dot"></span>LARKWELL</div>
<nav class="nav abs">
  <a style="left:507px">Home</a>
  <a style="left:600px">Services</a>
  <a style="left:710px">Products</a>
  <a style="left:823px">About us</a>
  <a style="left:936px">Blogs</a>
  <a style="left:1023px">Contact Us</a>
</nav>
<h1 class="hero-title abs">Save time and resources in cyber risk assessments</h1>
<p class="hero-sub abs">Calculate, reduce and monitor human cyber risk with the new-class of user-focused security.</p>
<a class="btn hero-btn abs">Learn more
  <svg viewBox="0 0 16 16" fill="none" stroke="#fff" stroke-width="1.8"><path d="M2 8h11M9 4l4 4-4 4"/></svg></a>

<!-- ABOUT -->
<div class="about-photo abs" role="img" aria-label="Photograph of a security analyst holding a tablet in a server room"></div>
<div class="about-eyebrow eyebrow-line abs">About Us <i style="flex:1;background:var(--line)"></i></div>
<h2 class="about-title abs">The tech you use to run your business could be used to sabotage it!</h2>
<p class="about-text abs" style="top:984px">In the course of doing business, your company could deal with dozens of third-party vendors: suppliers, manufacturers, service providers, affiliate offices, distributors, resellers, agents, contractors, the list goes on … all of whom, in turn, deal with dozens of their own vendors. It's easy to see then why third-party cyber risk management is becoming such a high priority for businesses that deal with confidential data. (Lawyers, accountants, insurers, to name just three.)</p>
<p class="about-text abs" style="top:1116px">Larkwell is a 100% New Zealand owned and operated cyber security company, designed to protect your business against exactly this kind of risk by offering third-party risk managementand cyber security solutions. In short, offering small and medium sized businesses the same standard of cyber security as a large organisations – at a price that makes sense.</p>
<a class="btn about-btn abs">Learn more
  <svg viewBox="0 0 16 16" fill="none" stroke="#fff" stroke-width="1.8"><path d="M2 8h11M9 4l4 4-4 4"/></svg></a>

<!-- SERVICES -->
<div class="section-head abs" style="top:1384px">
  <div class="eyebrow-line"><i></i>Larkwell<i></i></div>
  <h2>OUR SERVICES</h2>
</div>
<div class="svc-arrow abs" style="left:50px"><svg width="14" height="14" viewBox="0 0 14 14" fill="none" stroke="#58427c" stroke-width="2"><path d="M9 2 4 7l5 5"/></svg></div>
<div class="svc-arrow abs" style="left:1116px"><svg width="14" height="14" viewBox="0 0 14 14" fill="none" stroke="#58427c" stroke-width="2"><path d="M5 2l5 5-5 5"/></svg></div>

<div class="svc-card-hl abs"></div>
<div class="svc-icon abs" style="left:205px">
  <svg width="56" height="56" viewBox="0 0 56 56" fill="none" stroke="#58427c" stroke-width="2"><circle cx="20" cy="20" r="10"/><circle cx="20" cy="20" r="4"/><circle cx="34" cy="26" r="7"/><path d="M22 50c0-9 5-14 12-14s12 5 12 14"/></svg>
</div>
<div class="svc-icon dark abs" style="left:547px">
  <svg width="56" height="56" viewBox="0 0 56 56" fill="none" stroke="#fff" stroke-width="2"><rect x="8" y="12" width="40" height="28" rx="2"/><path d="M20 48h16M28 40v8"/><path d="M28 16l8 3v6c0 5-4 8-8 9-4-1-8-4-8-9v-6z"/></svg>
</div>
<div class="svc-icon abs" style="left:888px">
  <svg width="56" height="56" viewBox="0 0 56 56" fill="none" stroke="#58427c" stroke-width="2"><rect x="12" y="8" width="28" height="40" rx="2"/><path d="M18 18l3 3 5-5M18 30l3 3 5-5M30 20h6M30 32h6"/><path d="M40 30l8 16H32z"/></svg>
</div>

<div class="svc-title abs" style="left:118px">Virtual CISO</div>
<div class="svc-title abs on-dark" style="left:459px">Cyber Security assessments</div>
<div class="svc-title abs" style="left:800px">Third-party Risk Management</div>
<p class="svc-text abs" style="left:123px">Lorem Ipsum is simply dummy text of the printing and typesetting industry. Lorem Ipsum has been the industry's standard dummy text ever since the 1500s, when an unknown.</p>
<p class="svc-text abs on-dark" style="left:465px">Lorem Ipsum is simply dummy text of the printing and typesetting industry. Lorem Ipsum has been the industry's standard dummy text ever since the 1500s, when an unknown.</p>
<p class="svc-text abs" style="left:805px">Lorem Ipsum is simply dummy text of the printing and typesetting industry. Lorem Ipsum has been the industry's standard dummy text ever since the 1500s, when an unknown.</p>
<div class="svc-next abs"><svg width="12" height="12" viewBox="0 0 12 12" fill="none" stroke="#58427c" stroke-width="2"><path d="M1 6h9M7 3l3 3-3 3"/></svg></div>

<!-- PRODUCTS -->
<div class="section-head abs" style="top:1873px">
  <div class="eyebrow-line"><i></i>Larkwell<i></i></div>
  <h2>OUR PRODUCTS</h2>
</div>
<svg class="prod-icon abs" style="left:135px" viewBox="0 0 116 116" fill="none" stroke="#58427c" stroke-width="5"><circle cx="46" cy="42" r="22"/><circle cx="46" cy="36" r="7"/><path d="M34 54c3-7 21-7 24 0"/><circle cx="86" cy="76" r="22"/><circle cx="86" cy="70" r="7"/><path d="M74 88c3-7 21-7 24 0"/><path d="M100 10l10 18H90z" fill="#58427c"/></svg>
<svg class="prod-icon abs" style="left:408px" viewBox="0 0 116 116" fill="none" stroke="#58427c" stroke-width="5"><path d="M30 70a18 18 0 0 1 4-35 26 26 0 0 1 48 0 18 18 0 0 1 4 35z" fill="#58427c"/><path d="M58 32l14 6v12c0 10-7 16-14 18-7-2-14-8-14-18V38z" stroke="#fff" stroke-width="4"/><path d="M40 76v22h-8M76 76v22h8M58 70v30"/></svg>
<svg class="prod-icon abs" style="left:677px" viewBox="0 0 116 116" fill="none" stroke="#58427c" stroke-width="5"><rect x="14" y="12" width="80" height="64" rx="4"/><path d="M14 26h80"/><text x="26" y="54" font-family="Epilogue,sans-serif" font-size="16" fill="#58427c" stroke="none">0101</text><circle cx="74" cy="80" r="20" fill="#fff"/><path d="M88 94l14 14"/><rect x="66" y="78" width="16" height="12" rx="2"/><path d="M70 78v-4a4 4 0 0 1 8 0v4"/></svg>
<svg class="prod-icon abs" style="left:947px" viewBox="0 0 116 116" fill="#58427c"><path d="M14 62h18l6 12h40l6-12h18l-10 20-14 6-6 14h-28l-6-14-14-6z"/><rect x="40" y="40" width="36" height="30" rx="4"/><path d="M46 40v-8a12 12 0 0 1 24 0v8" fill="none" stroke="#58427c" stroke-width="6"/><circle cx="58" cy="54" r="4" fill="#fff"/><rect x="56" y="56" width="4" height="8" fill="#fff"/></svg>

<svg class="prod-link abs" style="left:290px" viewBox="0 0 84 30" fill="none" stroke="#9a8fb0" stroke-width="2" stroke-dasharray="2 4"><path d="M2 20C25 4 55 4 78 22"/><path d="M72 16l7 6-9 2" stroke-dasharray="none"/></svg>
<svg class="prod-link abs" style="left:557px" viewBox="0 0 84 30" fill="none" stroke="#9a8fb0" stroke-width="2" stroke-dasharray="2 4"><path d="M2 12C25 28 55 26 78 6"/><path d="M70 6l9 0-3 8" stroke-dasharray="none"/></svg>
<svg class="prod-link abs" style="left:828px" viewBox="0 0 84 30" fill="none" stroke="#9a8fb0" stroke-width="2" stroke-dasharray="2 4"><path d="M2 20C25 4 55 4 78 22"/><path d="M72 16l7 6-9 2" stroke-dasharray="none"/></svg>

<div class="prod-num abs" style="left:173px">1</div>
<div class="prod-num abs" style="left:446px">2</div>
<div class="prod-num abs" style="left:715px">3</div>
<div class="prod-num abs" style="left:985px">4</div>
<div class="prod-name abs" style="left:83px">Third Party<br>Risk Management</div>
<div class="prod-name abs" style="left:356px">Cirralon Cloud<br>Based Security</div>
<div class="prod-name abs" style="left:625px">Vulnerability<br>Management</div>
<div class="prod-name abs" style="left:895px">Vaultline Password<br>Management</div>

<!-- ARTICLES -->
<div class="section-head abs" style="top:2356px">
  <div class="eyebrow-line"><i></i>Larkwell<i></i></div>
  <h2>RECENT ARTICLES</h2>
</div>

<div class="art-photo big abs" role="img" aria-label="Photograph of an engineer working at multiple monitors in a dark office"><span class="date-tag">May 12, 2017</span></div>
<div class="abs" style="left:108px;top:2802px;width:480px">
  <div class="art-cat">Cyber Security</div>
  <h3 class="art-title" style="margin-top:12px">Lorem Ipsum is simply dummy text</h3>
  <p class="art-text" style="margin-top:8px">Lorem ipsum dolor sit amet, consectetur adipisicing elit, sed do eiusmod tempor incididunt ut labore et dolore magna aliqua. Ut enim.</p>
</div>
<a class="btn art-btn abs" style="left:106px;top:2916px">Learn more <svg viewBox="0 0 16 16" fill="none" stroke="#fff" stroke-width="1.8"><path d="M2 8h11M9 4l4 4-4 4"/></svg></a>

<div class="art-photo sm1 abs" role="img" aria-label="Photograph of hands typing on a laptop with a security padlock overlay"><span class="date-tag">May 12, 2017</span></div>
<div class="abs" style="left:882px;top:2483px;width:222px">
  <div class="art-cat">Cyber Security</div>
  <h3 class="art-title" style="margin-top:12px">Lorem Ipsum is simply dummy text</h3>
  <p class="art-text" style="margin-top:12px">Lorem ipsum dolor sit amet, consectetur adipisicing elit, sed do eiusmod tempor incididunt ut labore et dolore magna aliqua. Ut enim.</p>
</div>
<a class="btn art-btn abs" style="left:880px;top:2666px">Learn more <svg viewBox="0 0 16 16" fill="none" stroke="#fff" stroke-width="1.8"><path d="M2 8h11M9 4l4 4-4 4"/></svg></a>

<div class="art-photo sm2 abs" role="img" aria-label="Photograph of a laptop keyboard under a blue glowing padlock network graphic"><span class="date-tag">May 12, 2017</span></div>
<div class="abs" style="left:882px;top:2732px;width:222px">
  <div class="art-cat">Cyber Security</div>
  <h3 class="art-title" style="margin-top:12px">Lorem Ipsum is simply dummy text</h3>
  <p class="art-text" style="margin-top:12px">Lorem ipsum dolor sit amet, consectetur adipisicing elit, sed do eiusmod tempor incididunt ut labore et dolore magna aliqua. Ut enim.</p>
</div>
<a class="btn art-btn abs" style="left:880px;top:2915px">Learn more <svg viewBox="0 0 16 16" fill="none" stroke="#fff" stroke-width="1.8"><path d="M2 8h11M9 4l4 4-4 4"/></svg></a>

<!-- CONTACT FORM -->
<section class="contact abs" role="img" aria-label="Purple-tinted photograph of a city skyline"></section>
<div class="contact-shade abs"></div>
<div class="section-head abs" style="top:3083px;left:-12px">
  <div class="eyebrow-line" style="color:#fff"><i style="background:#fff"></i>Larkwell<i style="background:#fff"></i></div>
  <h2 style="color:#fff">CONTACT FORM</h2>
</div>
<div class="field abs" style="left:322px;top:3198px;width:275px;height:40px">FIRST NAME*</div>
<div class="field abs" style="left:604px;top:3198px;width:275px;height:40px">LAST NAME*</div>
<div class="field abs" style="left:322px;top:3250px;width:275px;height:40px">E-MAIL*</div>
<div class="field abs" style="left:604px;top:3250px;width:275px;height:40px">PHONE*</div>
<div class="field abs" style="left:322px;top:3302px;width:557px;height:128px">MESSAGE</div>
<div class="send abs">SEND NOW</div>

<!-- FOOTER -->
<div class="abs" style="left:98px;top:3596px">
  <div class="foot-h">QUICK LINKS</div>
  <div class="foot-links" style="margin-top:18px">Home<br>Services<br>Products<br>About us<br>Blogs<br>Contact Us</div>
</div>
<div class="foot-div abs" style="left:253px"></div>
<div class="abs" style="left:311px;top:3596px;width:210px">
  <div class="foot-h">CONTACT US</div>
  <div class="contact-row" style="margin-top:18px"><svg viewBox="0 0 16 16" fill="#58427c"><path d="M8 0a6 6 0 0 0-6 6c0 4 6 10 6 10s6-6 6-10a6 6 0 0 0-6-6zm0 8.5A2.5 2.5 0 1 1 8 3.5a2.5 2.5 0 0 1 0 5z"/></svg><span>42 Harrow Lane, Te Aro,<br>Wellington, 6011</span></div>
  <div class="contact-row" style="margin-top:26px"><svg viewBox="0 0 16 16"><circle cx="8" cy="8" r="8" fill="#58427c"/><path d="M5 4l2 2-1 1a5 5 0 0 0 3 3l1-1 2 2-1 1c-3 0-7-4-7-7z" fill="#fff"/></svg><span>+64 (0) 210 555 0142</span></div>
  <div class="contact-row" style="margin-top:34px"><svg viewBox="0 0 16 16"><circle cx="8" cy="8" r="8" fill="#58427c"/><rect x="4" y="5" width="8" height="6" fill="none" stroke="#fff"/><path d="M4 5l4 3 4-3" fill="none" stroke="#fff"/></svg><span>info@larkwell.co.nz</span></div>
</div>
<div class="foot-div abs" style="left:532px"></div>
<div class="map abs" role="img" aria-label="Street map showing the office location with a red pin"></div>
<div class="foot-div abs" style="left:817px"></div>
<div class="foot-mark abs"></div>
<div class="foot-brand abs">LARKWELL</div>
<div class="follow abs">Follow Us <span class="s"></span><span class="s"></span><span class="s"></span></div>

<div class="bottom-bar abs">© Copyright - 2022 &nbsp;| &nbsp;Larkwell &nbsp;| &nbsp;All Rights Reserved</div>

</body>
</html>
```